Brennick Holdings Business Cards

These are professional business cards that are for my family office.
Put fake emails and phone numbers as of now until I finalize those components. This family office controls my families investments, assets, and future. The cards should be professional.
..
.
.
.
I just uploaded another variation of a logo I would like to see as a business card to I am inbeteen which logo to use

Target Market(s)

business

Industry/Entity Type

business

Contact Information for Business Card

Professional, wealth related, finance related.

Requirements
Must have
• Logo

```html
<!DOCTYPE html>
<html lang="en">
<head>
<meta charset="utf-8">
<title>Brennick Holdings – Business Cards</title>
<link rel="stylesheet" href="https://fonts.googleapis.com/css2?family=Tinos:wght@400;700&display=swap">
<style>
  :root {
    --backdrop: #9a9899;
    --card: #ffffff;
    --navy: #1a1d2b;
    --grey-text: #8f8f91;
    --grey-name: #9d9d9f;
    --pale: #f1f1f3;
    --pale-dot: #e9e9ec;
  }
  * { margin: 0; padding: 0; box-sizing: border-box; }
  html, body {
    width: 1200px; height: 1200px; overflow: hidden;
    background: var(--backdrop);
    font-family: "Tinos", "Times New Roman", serif;
  }
  .canvas { position: relative; width: 1200px; height: 1200px; }
  .card {
    position: absolute; left: 166px; width: 868px; height: 508px;
    background: var(--card); overflow: hidden;
  }
  .card--front { top: 71px; }
  .card--back { top: 615px; }

  .front-pattern {
    position: absolute; left: 0; top: 0; width: 304px; height: 100%;
    background: var(--pale);
  }
  .front-info {
    position: absolute; right: 78px; top: 0; bottom: 0; width: 520px;
    text-align: right; color: var(--grey-text);
  }
  .front-info > * { position: absolute; right: 0; line-height: 1; white-space: nowrap; }
  .brand-name {
    color: var(--navy); font-weight: 400; font-variant: small-caps;
    letter-spacing: 0.5px; line-height: 1; white-space: nowrap;
  }
  .front-info .brand-name { top: 84px; font-size: 44px; }
  .person-name {
    top: 258px; font-size: 34px; font-weight: 700;
    color: var(--grey-name); letter-spacing: 1px;
  }
  .person-role { top: 308px; font-size: 21px; }
  .contact { top: 380px; list-style: none; font-size: 21px; }
  .contact li {
    display: flex; align-items: center; justify-content: flex-end;
    gap: 12px; height: 33px; line-height: 33px;
  }
  .contact svg { width: 16px; height: 16px; fill: var(--grey-text); }

  .back-ring { position: absolute; left: 0; top: 0; width: 868px; height: 508px; }
  .back-dot {
    position: absolute; left: 475px; top: 286px; width: 98px; height: 98px;
    border-radius: 50%; background: var(--pale-dot);
  }
  .back-mark {
    position: absolute; left: 167px; top: 209px; width: 142px; height: 142px;
    border: 3px solid var(--navy); border-radius: 50%;
  }
  .card--back .brand-name {
    position: absolute; left: 238px; top: 371px; font-size: 29px;
    transform: translateX(-50%);
  }
</style>
</head>
<body>
<main class="canvas">
  <section class="card card--front">
    <div class="front-pattern" role="img" aria-label="Light grey repeating ring-and-dot pattern panel"></div>
    <div class="front-info">
      <div class="brand-name">Brennick Holdings</div>
      <div class="person-name">JULIAN HARTLEY</div>
      <div class="person-role">Director/electrician</div>
      <ul class="contact">
        <li>555 0142 876
          <svg viewBox="0 0 16 16" aria-hidden="true"><path d="M4 0h8a1 1 0 0 1 1 1v14a1 1 0 0 1-1 1H4a1 1 0 0 1-1-1V1a1 1 0 0 1 1-1zm1 2v10h6V2zm3 11a1 1 0 1 0 0 2 1 1 0 0 0 0-2z"/></svg>
        </li>
        <li>info@brennickholdings.com
          <svg viewBox="0 0 16 16" aria-hidden="true"><path d="M1 3h14v10H1zM2 4l6 5 6-5z" fill-rule="evenodd"/></svg>
        </li>
      </ul>
    </div>
  </section>

  <section class="card card--back">
    <svg class="back-ring" viewBox="0 0 868 508" aria-hidden="true">
      <circle cx="834" cy="35" r="232" fill="none" stroke="#f1f1f3" stroke-width="116"/>
    </svg>
    <div class="back-dot"></div>
    <div class="back-mark"></div>
    <div class="brand-name">Brennick Holdings</div>
  </section>
</main>
</body>
</html>
```